Lucien business card

Business card for commercial photography , photographer specialized in advertising, architecture and interior photography, adventure imagery and camera work. 40 years old, worked for the last 20 years. Business card needs to convey a sense of confidence in work achieved. Card needs to be eye catching as will be left behind in many people's offices. Should also mention discreetly NRVB accredited photographer at the verso of the card. Phone number and website link must be apparent easily.

Target Market(s)

Advertising agencies, commercial photography representation

Industry/Entity Type

Architecture

Contact Information for Business Card

Phone number : +61 470 918 264
lucien.marvaux@velmora.example
www.lucienmarvaux.example

Font styles to use
Sans Serif

Requirements
Must have
• Email adress
• Website
• Phone number
• Name
• Photographer
Nice to have
• NRVB accredited photographer
Should not have
• Rond corners

```html
<!DOCTYPE html>
<html lang="en">
<head>
<meta charset="utf-8">
<title>Lucien business card</title>
<link href="https://fonts.googleapis.com/css2?family=Jost:wght@400&display=swap" rel="stylesheet">
<style>
  :root {
    --page: #ffffff;
    --card: #ffffff;
    --edge: #6b6b6b;
    --ink: #1c1c1c;
    --accent: #d32f2f;
  }
  html, body {
    margin: 0;
    padding: 0;
    width: 1200px;
    height: 1000px;
    overflow: hidden;
    background: var(--page);
  }
  .canvas {
    position: relative;
    width: 1200px;
    height: 1000px;
    font-family: "Jost", "Futura", sans-serif;
    color: var(--ink);
  }
  .card {
    position: absolute;
    left: 76px;
    top: 200px;
    width: 1048px;
    height: 598px;
    border: 1px solid var(--edge);
    background: var(--card);
  }
  .brand-mark {
    position: absolute;
    left: 0;
    right: 0;
    top: 100px;
    display: flex;
    justify-content: center;
    align-items: center;
    gap: 12px;
  }
  .brand-mark .dot {
    width: 14px;
    height: 14px;
    background: var(--accent);
  }
  .brand-mark .wordmark {
    font-size: 64px;
    line-height: 1;
    letter-spacing: 2px;
    color: var(--ink);
  }
  .identity {
    position: absolute;
    left: 0;
    right: 0;
    top: 292px;
    text-align: center;
  }
  .name {
    margin: 0;
    font-size: 52px;
    line-height: 56px;
    font-weight: 400;
    letter-spacing: 3px;
  }
  .name .surname { color: var(--accent); }
  .accreditation {
    margin: 0;
    font-size: 27px;
    line-height: 30px;
    word-spacing: 6px;
  }
  .phone {
    margin: 6px 0 0;
    font-size: 34px;
    line-height: 40px;
    word-spacing: 8px;
  }
  .contact-line {
    position: absolute;
    left: 0;
    right: 0;
    top: 532px;
    text-align: center;
    font-size: 33px;
    line-height: 40px;
  }
  .contact-line .divider {
    color: var(--accent);
    margin: 0 22px;
  }
</style>
</head>
<body>
<div class="canvas">
  <section class="card">
    <div class="brand-mark">
      <span class="wordmark">LM</span>
      <span class="dot"></span>
    </div>
    <div class="identity">
      <h1 class="name">LUCIEN<span class="surname">MARVAUX</span></h1>
      <p class="accreditation">(NRVB accredited photographer)</p>
      <p class="phone">+61 470 918 264</p>
    </div>
    <div class="contact-line">
      <span class="email">lucien.marvaux@velmora.example</span><span class="divider">|</span><span class="website">www.lucienmarvaux.example</span>
    </div>
  </section>
</div>
</body>
</html>
```